Bref créative
Modern stationary/business card design for KMR Interior Solutions
KMR Interior Solutions
Modern
Dolan Prewitt
VP
7428 B Fernvale
Marlow Creek, TX 75294
dolan@cresthollowstone.com
www.cresthollowstone.com
We are open to tag lines so feel free to explore. I will give feedback to point you in the right direction.
Possibly a list of all the services we provide...
Granite, Quartz, Tile, Vinyl, Wood, Carpet, Mirrors, Cabinets, Hardware
I have more colors to choose from.

```html
<!DOCTYPE html>
<html lang="en">
<head>
<meta charset="utf-8">
<title>KMR Interior Solutions — Stationery</title>
<link href="https://fonts.googleapis.com/css2?family=Open+Sans:wght@300;400;600&display=swap" rel="stylesheet">
<style>
:root{
  --bg:#ebecec;
  --paper:#ffffff;
  --olive:#a8a23a;
  --olive-dark:#8f8a2c;
  --olive-faint:#ecebd6;
  --grey:#8d8d8d;
  --grey-light:#c9c9c9;
  --ink:#5a5a5a;
}
*{box-sizing:border-box;margin:0;padding:0}
html,body{width:1200px;height:936px;overflow:hidden}
body{background:var(--bg);font-family:"Open Sans",Arial,sans-serif;color:var(--ink);position:relative}
address{font-style:normal}
.sheet{position:absolute;background:var(--paper);box-shadow:0 2px 6px rgba(0,0,0,.12)}
.footer-band{position:absolute;left:0;right:0;background:var(--olive);color:#fff;text-align:center;letter-spacing:.18em;font-weight:400;white-space:nowrap;overflow:hidden}
.footer-rule{position:absolute;left:0;right:0;height:2px;background:var(--grey-light)}
.mark{display:flex;align-items:center;gap:6px}
.mark-square{background:var(--olive);flex:none}
.mark-name{color:var(--olive);font-weight:400;line-height:1}
.mark-sub{color:var(--olive);font-weight:300;line-height:1.1;white-space:nowrap}

/* Letterhead */
.letterhead{left:183px;top:63px;width:388px;height:554px}
.letterhead .mark{position:absolute;left:20px;top:30px}
.letterhead .mark-square{width:16px;height:16px}
.letterhead .mark-name{font-size:15px}
.letterhead .mark-sub{font-size:8px}
.contact-block{position:absolute;right:20px;top:26px;font-size:6px;line-height:9px;color:var(--grey)}
.contact-block span{display:block}
.watermark{position:absolute;left:50%;top:250px;transform:translateX(-50%);font-size:54px;font-weight:300;color:var(--olive-faint);letter-spacing:.05em}
.letterhead .footer-band{bottom:16px;height:14px;font-size:8px;line-height:14px}
.letterhead .footer-rule{bottom:10px}

/* Folder */
.folder{left:634px;top:38px;width:462px;height:579px}
.folder-mark{position:absolute;left:0;right:0;top:140px;display:flex;flex-direction:column;align-items:center}
.folder-mark .mark-square{width:56px;height:56px;margin-bottom:18px}
.folder-mark .mark-name{font-size:64px;letter-spacing:.02em}
.folder-mark .mark-sub{font-size:24px;margin-top:4px}
.folder .footer-band{bottom:24px;height:20px;font-size:10px;line-height:20px}
.folder .footer-rule{bottom:16px;height:3px}

/* Business cards */
.card{left:36px;width:210px;height:110px}
.card-front{top:672px}
.card-front .mark{position:absolute;left:12px;top:12px;flex-direction:column;align-items:flex-start;gap:3px}
.card-front .mark-square{width:12px;height:12px}
.card-front .mark-name{font-size:11px}
.card-front .mark-sub{font-size:6px}
.card-details{position:absolute;left:66px;top:14px;font-size:6px;line-height:9px;color:var(--grey)}
.card-details .person{color:var(--ink);font-weight:600}
.card-front .footer-band{bottom:8px;height:8px;font-size:5px;line-height:8px}
.card-back{top:794px;background:var(--olive)}
.card-pattern{position:absolute;left:40px;top:14px;width:80px;height:80px;background:linear-gradient(135deg,#bdb85a,var(--olive-dark))}

/* Envelope front */
.envelope{top:672px;height:208px}
.envelope-front{left:266px;width:432px}
.envelope-front .mark{position:absolute;left:16px;top:18px}
.envelope-front .mark-square{width:22px;height:22px}
.envelope-front .mark-name{font-size:20px}
.envelope-front .mark-sub{font-size:9px}
.return-address{position:absolute;left:16px;top:64px;font-size:6px;color:var(--grey)}
.envelope-front .footer-band{bottom:34px;height:16px;font-size:8px;line-height:16px}

/* Envelope back */
.envelope-back{left:736px;width:431px}
.envelope-back svg{position:absolute;left:0;top:0}
.flap-url{position:absolute;left:0;right:0;top:18px;text-align:center;font-size:9px;letter-spacing:.18em;color:#fff}
</style>
</head>
<body>

<section class="sheet letterhead" aria-label="Letterhead">
  <div class="mark">
    <span class="mark-square"></span>
    <div><div class="mark-name">KMR</div><div class="mark-sub">Interior Solutions</div></div>
  </div>
  <address class="contact-block">
    <span>7428 B Fernvale</span>
    <span>Marlow Creek, TX 75294</span>
    <span>T 713.555.0142</span>
    <span>F 713.555.0143</span>
    <span>dolan@cresthollowstone.com</span>
  </address>
  <div class="watermark" aria-hidden="true">KMR</div>
  <div class="footer-band">www.cresthollowstone.com</div>
  <div class="footer-rule"></div>
</section>

<section class="sheet folder" aria-label="Presentation folder">
  <div class="folder-mark">
    <span class="mark-square"></span>
    <div class="mark-name">KMR</div>
    <div class="mark-sub">Interior Solutions</div>
  </div>
  <div class="footer-band">www.cresthollowstone.com</div>
  <div class="footer-rule"></div>
</section>

<section class="sheet card card-front" aria-label="Business card front">
  <div class="mark">
    <span class="mark-square"></span>
    <div class="mark-name">KMR</div>
    <div class="mark-sub">Interior Solutions</div>
  </div>
  <address class="card-details">
    <div class="person">Dolan Prewitt</div>
    <div>VP</div>
    <div>7428 B Fernvale</div>
    <div>Marlow Creek, TX 75294</div>
    <div>M 713.555.0199</div>
    <div>dolan@cresthollowstone.com</div>
  </address>
  <div class="footer-band">www.cresthollowstone.com</div>
</section>

<section class="sheet card card-back" aria-label="Business card back">
  <div class="card-pattern" role="img" aria-label="Faceted geometric pattern in olive tones"></div>
</section>

<section class="sheet envelope envelope-front" aria-label="Envelope front">
  <div class="mark">
    <span class="mark-square"></span>
    <div><div class="mark-name">KMR</div><div class="mark-sub">Interior Solutions</div></div>
  </div>
  <address class="return-address">7428 B Fernvale, Marlow Creek, TX 75294</address>
  <div class="footer-band">www.cresthollowstone.com</div>
</section>

<section class="sheet envelope envelope-back" aria-label="Envelope back">
  <svg width="431" height="208" viewBox="0 0 431 208" aria-hidden="true">
    <path d="M0 0 H431 V40 Q431 60 400 66 L216 100 L31 66 Q0 60 0 40 Z" fill="var(--olive)"/>
  </svg>
  <div class="flap-url">www.cresthollowstone.com</div>
</section>

</body>
</html>
```